Terraquest NW PPT template - non-profit company - minerals, energy, water, geothermal resources

Terraquest NW requires two (Letter-sized and 16:9)simple, flexible and clean PowerPoint templates that can be used for corporate and research project presentations and meeting materials

Each layout should have correct colours, fonts and size as a default (focus area colours for headings; secondary colours for body text). Each slide should have the Terraquest NW logo. Slide number should be automatically generated, with no slide number on title slide.

Target Market(s)

Varied, but almost always professional: Government; Community leaders; Mineral/Energy industries; and Academic researchers.

Font styles to use
Serif
Sans Serif
Other font styles liked:
• Calibri, or whatever in style guide

Requirements
Must have
• Two version that we can use – both need to match:
- 16:9 slide size for on-screen presentations; and
- Letter (8.5 x 11 inch) for meeting materials that are printed.

Must use colours in logo as listed in the style guide
Nice to have
• Consistency
Should not have
• Should not be black and white - needs colour

```html
<!DOCTYPE html>
<html lang="en">
<head>
<meta charset="utf-8">
<title>Terraquest NW – Presentation Template</title>
<link rel="stylesheet" href="https://fonts.googleapis.com/css2?family=Open+Sans:wght@400;600;700&display=swap">
<style>
:root{
  --orange:#e07b3f;
  --green:#00a94f;
  --teal:#22a3c4;
  --slate:#4a5058;
  --gold:#e2b04a;
  --navy:#22478a;
  --ink:#4d5259;
  --muted:#8a8f96;
  --rule:#e3e4e6;
  --canvas:#ececec;
}
*{box-sizing:border-box;margin:0;padding:0}
html,body{width:1200px;height:3200px;overflow:hidden}
body{background:var(--canvas);font-family:"Open Sans",Arial,sans-serif;color:var(--ink);position:relative}

.hero-frame{position:absolute;left:100px;top:60px;width:1001px;height:564px;box-shadow:0 10px 30px rgba(0,0,0,.18)}
.hero-frame .slide{transform:scale(2.75);transform-origin:0 0;box-shadow:none}

.deck{position:absolute;left:38px;top:700px;display:grid;grid-template-columns:repeat(3,364px);column-gap:16px;row-gap:22px}

.slide{position:relative;width:364px;height:205px;background:#fff;overflow:hidden;box-shadow:0 2px 6px rgba(0,0,0,.12)}
.stripe{position:absolute;left:0;right:0;bottom:0;height:3px;
  background:linear-gradient(90deg,var(--orange) 0 20%,var(--green) 20% 40%,var(--teal) 40% 60%,var(--slate) 60% 80%,var(--gold) 80%)}
.foot-brand{position:absolute;left:14px;bottom:7px;font-size:4.5px;font-weight:700;color:var(--slate)}
.page-no{position:absolute;right:12px;bottom:7px;font-size:4px;color:var(--muted)}

.brand{display:flex;align-items:center;gap:4px;font-weight:700;color:var(--slate)}
.brand-mark{width:7px;height:7px;background:var(--orange)}
.on-colour .brand{color:#fff}
.on-colour .brand-mark{background:#fff}

.photo-wash{position:absolute}

.slide-title{position:absolute;left:18px;top:14px;font-size:10px;font-weight:600;color:var(--slate);letter-spacing:.2px}
.kicker{font-size:5.5px;font-weight:600;color:var(--orange);text-transform:uppercase}
.body{font-size:4.8px;line-height:1.5;color:var(--ink)}
.body ul{list-style:none}
.body li{position:relative;padding-left:6px;margin-top:2px}
.body li::before{content:"•";position:absolute;left:0;color:var(--teal)}
.body li.sub{padding-left:14px;color:var(--muted)}
.body li.sub::before{content:"–";left:8px;color:var(--muted)}

/* title slides */
.cover .brand{position:absolute;left:26px;top:38px;font-size:11px}
.cover .cover-rule{position:absolute;left:26px;top:72px;width:14px;height:1.2px;background:var(--orange)}
.cover h1{position:absolute;left:26px;top:76px;font-size:13px;font-weight:600;color:var(--slate)}
.cover .cover-sub{position:absolute;left:26px;top:93px;font-size:6px;color:var(--orange)}
.cover .cover-date{position:absolute;left:26px;top:104px;font-size:4px;color:var(--muted)}
.icon-row{position:absolute;right:8px;bottom:10px;display:grid;grid-template-columns:repeat(4,9px);gap:3px}
.icon-row i{width:9px;height:9px;border:1px solid currentColor;border-radius:50%;display:block}

.cover-dark{background:linear-gradient(160deg,#5c6168,#474c53)}
.cover-dark h1,.cover-dark .brand{color:#fff}
.cover-dark .cover-sub,.cover-dark .cover-date{color:#e6e6e6}

.cover-band .band{position:absolute;left:18px;top:86px;width:240px;height:36px;background:var(--orange)}
.cover-band .band h1{position:static;font-size:8.5px;color:#fff;padding:6px 0 0 8px}
.cover-band .band p{font-size:4.5px;color:#fff;padding-left:8px}

/* dividers */
.divider .brand{position:absolute;left:16px;top:38px;font-size:8px}
.divider .div-icon{position:absolute;left:16px;top:100px;width:14px;height:14px}
.divider h2{position:absolute;left:16px;top:126px;font-size:7px;font-weight:600;color:#fff}
.divider .div-sub{position:absolute;left:16px;top:136px;font-size:4.5px;color:#fff}
.divider .ridge-wash{position:absolute;right:14px;bottom:8px;width:150px;height:60px;
  background:radial-gradient(ellipse at 55% 100%,rgba(0,0,0,.1) 0,rgba(0,0,0,.05) 45%,transparent 72%)}

/* content blocks */
.col{position:absolute;top:36px}
.bar-list{position:absolute;left:18px;right:18px;top:44px;display:grid;gap:4px}
.bar-list div{background:#e9eaeb;border-left:3px solid var(--orange);padding:3px 6px;font-size:4.5px;line-height:1.5}
.tiles{position:absolute;left:18px;right:18px;top:48px;height:100px;display:grid;grid-template-columns:repeat(4,1fr);gap:6px}
.tile{color:#fff;text-align:center;padding:10px 4px 0;font-size:4px;line-height:1.5}
.tile svg{width:14px;height:14px;display:block;margin:0 auto 4px}
.tile b{display:block;font-size:4.5px}

.right-col .pic{position:absolute;left:18px;width:60px;height:50px}
.right-col .pic-note{position:absolute;left:78px;width:60px;height:50px;color:#fff;font-size:4px;padding:6px;line-height:1.5}

table.sample{position:absolute;left:18px;right:18px;top:40px;width:328px;border-collapse:collapse;font-size:3.6px}
table.sample th{background:var(--orange);color:#fff;font-size:4.5px;padding:3px;font-weight:600}
table.sample td{padding:3px;vertical-align:top;color:var(--ink);line-height:1.4}
table.sample tr:nth-child(odd) td{background:#ececed}

.services{position:absolute;left:30px;right:30px;top:40px;display:grid;grid-template-columns:repeat(3,1fr);row-gap:8px;text-align:center}
.svc .dot{width:16px;height:16px;border-radius:50%;margin:0 auto 3px;display:flex;align-items:center;justify-content:center}
.svc .dot span{width:6px;height:6px;border:1px solid #fff;border-radius:50%}
.svc b{display:block;font-size:4.5px;font-weight:600}
.svc p{font-size:3.6px;color:var(--muted)}

.chart-cap{position:absolute;left:0;right:0;top:36px;text-align:center;font-size:5px;font-weight:600;color:var(--slate)}
.pie{position:absolute;left:132px;top:46px;width:100px;height:100px;border-radius:50%;
  background:conic-gradient(var(--orange) 0 58%,var(--green) 58% 81%,var(--teal) 81% 91%,var(--slate) 91%)}
.pie-lbl{position:absolute;font-size:5px;font-weight:700;color:#fff}
.callout{position:absolute;font-size:3.6px;color:var(--muted);line-height:1.4}
.callout b{color:var(--ink);font-weight:600}
.legend{position:absolute;left:0;right:0;bottom:16px;text-align:center;font-size:3.4px;color:var(--muted)}

.bars{position:absolute;left:40px;right:30px;top:50px;height:92px;display:flex;align-items:flex-end;justify-content:space-around;border-left:.5px solid var(--rule);border-bottom:.5px solid var(--rule)}
.bars i{width:18px;display:block}
.bar-axis{position:absolute;left:40px;right:30px;top:145px;display:flex;justify-content:space-around;font-size:3.4px;color:var(--muted)}

.timeline{position:absolute;left:18px;right:18px;top:100px;height:1px;background:var(--muted)}
.tl-note{position:absolute;width:46px;height:26px;color:#fff;font-size:3.4px;line-height:1.4;padding:3px}
.tl-note b{display:block;font-size:3.8px}
.tl-lbl{position:absolute;font-size:4px;color:var(--ink)}
.tl-dot{position:absolute;top:98px;width:5px;height:5px;border-radius:50%;background:var(--slate)}

.map-wash{position:absolute;left:40px;top:34px;width:300px;height:130px;background:radial-gradient(ellipse at 50% 50%,#e6e7e9 0 55%,transparent 70%)}
.stat{position:absolute;border-radius:50%;color:#fff;font-weight:700;display:flex;align-items:center;justify-content:center;opacity:.9}

.hub{position:absolute;left:152px;top:62px;width:60px;height:60px;border:.6px solid var(--rule);border-radius:50%}
.node{position:absolute;width:13px;height:13px;border-radius:50%;border:1.2px solid}
.hub-label{position:absolute;left:160px;top:89px;font-size:4px;font-weight:700;color:var(--slate)}
.node-text{position:absolute;font-size:3.8px;color:var(--muted);width:70px;line-height:1.4}

.thanks{background:linear-gradient(160deg,#5c6168,#474c53)}
.thanks .strip{position:absolute;left:0;right:0;top:64px;height:56px;background:rgba(220,222,224,.85)}
.thanks h2{position:absolute;left:0;right:0;top:48px;text-align:center;color:#fff;font-size:9.5px;font-weight:600}
.contact{position:absolute;top:74px;width:70px;text-align:center;font-size:3.6px;color:var(--slate);line-height:1.4}
.contact b{display:block;font-size:4px}
.contact svg{width:7px;height:7px;display:block;margin:0 auto 2px}
.thanks .closing{position:absolute;left:0;right:0;top:130px;text-align:center;font-size:4.4px;color:#fff;line-height:1.5}
</style>
</head>
<body>

<div class="hero-frame">
  <section class="slide cover">
    <div class="photo-wash" role="img" aria-label="Faint grey photo of a survey drone in flight" style="right:0;top:0;width:180px;height:150px;background:radial-gradient(ellipse at 60% 35%,#e4e4e4 0,#f4f4f4 45%,#fff 75%)"></div>
    <div class="brand"><span class="brand-mark"></span>Terraquest NW</div>
    <div class="cover-rule"></div>
    <h1>GEOSCIENCE PRESENTATION</h1>
    <div class="cover-sub">Sub Presentation Title</div>
    <div class="icon-row">
      <i style="color:var(--orange)"></i><i style="color:var(--green)"></i><i style="color:var(--teal)"></i><i style="color:transparent;border:0"></i>
      <i style="color:var(--slate)"></i><i style="color:var(--gold)"></i><i style="color:var(--green)"></i><i style="color:var(--slate)"></i>
    </div>
    <div class="stripe"></div>
  </section>
</div>

<main class="deck">

  <section class="slide cover">
    <div class="photo-wash" role="img" aria-label="Faint grey photo of a survey drone in flight" style="right:0;top:0;width:180px;height:150px;background:radial-gradient(ellipse at 60% 35%,#e4e4e4 0,#f4f4f4 45%,#fff 75%)"></div>
    <div class="brand"><span class="brand-mark"></span>Terraquest NW</div>
    <div class="cover-rule"></div>
    <h1>GEOSCIENCE PRESENTATION</h1>
    <div class="cover-sub">Sub Presentation Title</div>
    <div class="icon-row">
      <i style="color:var(--orange)"></i><i style="color:var(--green)"></i><i style="color:var(--teal)"></i><i style="color:transparent;border:0"></i>
      <i style="color:var(--slate)"></i><i style="color:var(--gold)"></i><i style="color:var(--green)"></i><i style="color:var(--slate)"></i>
    </div>
    <div class="stripe"></div>
  </section>

  <section class="slide cover cover-dark">
    <div class="photo-wash" role="img" aria-label="Muted photo of a helicopter over a forested slope" style="inset:0;background:radial-gradient(ellipse at 62% 60%,rgba(255,255,255,.08),transparent 60%)"></div>
    <div class="brand"><span class="brand-mark"></span>Terraquest NW</div>
    <h1>GEOSCIENCE PRESENTATION</h1>
    <div class="cover-sub">Sub Presentation Title</div>
    <div class="cover-date" style="top:108px">April, 2020</div>
    <div class="icon-row">
      <i style="color:var(--orange)"></i><i style="color:var(--green)"></i><i style="color:var(--teal)"></i><i style="color:transparent;border:0"></i>
      <i style="color:#aaa"></i><i style="color:var(--gold)"></i><i style="color:var(--green)"></i><i style="color:#aaa"></i>
    </div>
    <div class="stripe"></div>
  </section>

  <section class="slide cover cover-band">
    <div class="brand" style="top:42px"><span class="brand-mark"></span>Terraquest NW</div>
    <div class="band"><h1>GEOSCIENCE PRESENTATION</h1><p>Sub Presentation Title</p><p style="margin-top:4px">April, 2020</p></div>
    <div class="stripe"></div>
  </section>

  <section class="slide divider on-colour" style="background:var(--orange)">
    <div class="brand"><span class="brand-mark"></span>Terraquest NW</div>
    <svg class="div-icon" viewBox="0 0 14 14" fill="none" stroke="#fff" stroke-width="1"><path d="M2 4 Q7 0 12 4"/><path d="M7 2 L3 13"/></svg>
    <h2>DIVIDER PRESENTATION</h2><div class="div-sub">Sub Heading</div>
    <div class="ridge-wash" role="img" aria-label="Faint mountain-range watermark"></div>
    <div class="stripe"></div>
  </section>

  <section class="slide divider on-colour" style="background:var(--green)">
    <div class="brand"><span class="brand-mark"></span>Terraquest NW</div>
    <svg class="div-icon" viewBox="0 0 14 14" fill="none" stroke="#fff" stroke-width="1"><circle cx="7" cy="6" r="4"/><path d="M5 11h4M5.5 13h3"/></svg>
    <h2>DIVIDER PRESENTATION</h2><div class="div-sub">Sub Heading</div>
    <div class="ridge-wash" role="img" aria-label="Faint mountain-range watermark"></div>
    <div class="stripe"></div>
  </section>

  <section class="slide divider on-colour" style="background:var(--teal)">
    <div class="brand"><span class="brand-mark"></span>Terraquest NW</div>
    <svg class="div-icon" viewBox="0 0 14 14" fill="none" stroke="#fff" stroke-width="1"><path d="M7 1 C7 1 3 7 3 9 A4 4 0 0 0 11 9 C11 7 7 1 7 1Z"/></svg>
    <h2>DIVIDER PRESENTATION</h2><div class="div-sub">Sub Heading</div>
    <div class="ridge-wash" role="img" aria-label="Faint mountain-range watermark"></div>
    <div class="stripe"></div>
  </section>

  <section class="slide divider on-colour" style="background:var(--slate)">
    <div class="brand"><span class="brand-mark"></span>Terraquest NW</div>
    <svg class="div-icon" viewBox="0 0 14 14" fill="none" stroke="#fff" stroke-width="1"><rect x="3" y="2" width="8" height="11"/><path d="M5 5h4M5 7.5h4M5 10h4"/></svg>
    <h2>DIVIDER PRESENTATION</h2><div class="div-sub">Sub Heading</div>
    <div class="ridge-wash" role="img" aria-label="Faint mountain-range watermark"></div>
    <div class="stripe"></div>
  </section>

  <section class="slide divider on-colour" style="background:var(--gold)">
    <div class="brand"><span class="brand-mark"></span>Terraquest NW</div>
    <svg class="div-icon" viewBox="0 0 14 14" fill="none" stroke="#fff" stroke-width="1"><circle cx="7" cy="5" r="3"/><path d="M2 13 Q7 7 12 13Z"/></svg>
    <h2>DIVIDER PRESENTATION</h2><div class="div-sub">Sub Heading</div>
    <div class="ridge-wash" role="img" aria-label="Faint mountain-range watermark"></div>
    <div class="stripe"></div>
  </section>

  <section class="slide">
    <h3 class="slide-title">ONE COLUMN</h3>
    <div class="col body" style="left:18px;right:18px;top:30px">
      <div class="kicker">Lorem ipsum</div>
      <ul>
        <li>Lorem ipsum dolor sit amet, te ullum corpora delicata duo. Rebum insolens pri eu. No alia tota modus qui.</li>
        <li class="sub">Sint brute at usu. Duo lisque appareat adversarium at.</li>
        <li>Lorem ipsum dolor sit amet, te ullum corpora delicata duo. Rebum insolens pri eu. No alia tota modus qui.</li>
        <li class="sub">Sint brute at usu. Duo lisque appareat adversarium at.</li>
        <li>Lorem ipsum dolor sit amet, te ullum corpora delicata duo. Rebum insolens pri eu. No alia tota modus qui.</li>
        <li class="sub">Sint brute at usu. Duo lisque appareat adversarium at.</li>
      </ul>
    </div>
    <div class="foot-brand">Terraquest NW</div><div class="page-no">9</div><div class="stripe"></div>
  </section>

  <section class="slide">
    <h3 class="slide-title">TWO COLUMN</h3>
    <div class="col body" style="left:18px;width:150px;top:30px">
      <div class="kicker">Lorem ipsum</div>
      <ul>
        <li>Lorem ipsum dolor sit amet, te ullum corpora delicata duo. Rebum insolens pri eu. No alia tota modus qui.</li>
        <li class="sub">Sint brute at usu. Duo lisque appareat adversarium at.</li>
        <li>Lorem ipsum dolor sit amet, te ullum corpora delicata duo. Rebum insolens pri eu. No alia tota modus qui.</li>
        <li class="sub">Sint brute at usu. Duo lisque appareat adversarium at.</li>
      </ul>
    </div>
    <div class="col body" style="left:190px;width:150px;top:30px">
      <div class="kicker">Lorem ipsum</div>
      <ul>
        <li>Lorem ipsum dolor sit amet, te ullum corpora delicata duo. Rebum insolens pri eu. No alia tota modus qui.</li>
        <li class="sub">Sint brute at usu. Duo lisque appareat adversarium at.</li>
        <li>Lorem ipsum dolor sit amet, te ullum corpora delicata duo. Rebum insolens pri eu. No alia tota modus qui.</li>
        <li class="sub">Sint brute at usu. Duo lisque appareat adversarium at.</li>
      </ul>
    </div>
    <div class="foot-brand">Terraquest NW</div><div class="page-no">10</div><div class="stripe"></div>
  </section>

  <section class="slide">
    <h3 class="slide-title">ONE COLUMN AND CONTENT</h3>
    <div class="kicker" style="position:absolute;left:18px;top:32px">Lorem ipsum:</div>
    <div class="bar-list">
      <div>Lorem ipsum dolor sit amet, te ullum corpora delicata duo. Rebum insolens pri eu.<br>No alia tota modus qui.</div>
      <div style="border-color:var(--green);background:#f3f3f4">Lorem ipsum dolor sit amet, te ullum corpora delicata duo. Rebum insolens pri eu.<br>No alia tota modus qui.</div>
      <div style="border-color:var(--teal)">Lorem ipsum dolor sit amet, te ullum corpora delicata duo. Rebum insolens pri eu.<br>No alia tota modus qui.</div>
      <div style="border-color:var(--slate);background:#f3f3f4">Lorem ipsum dolor sit amet, te ullum corpora delicata duo. Rebum insolens pri eu.<br>No alia tota modus qui.</div>
    </div>
    <div class="foot-brand">Terraquest NW</div><div class="page-no">11</div><div class="stripe"></div>
  </section>

  <section class="slide">
    <h3 class="slide-title">ONE COLUMN AND CONTENT</h3>
    <div class="kicker" style="position:absolute;left:18px;top:32px">Lorem ipsum:</div>
    <div class="tiles">
      <div class="tile" style="background:var(--orange)"><svg viewBox="0 0 14 14" fill="none" stroke="#fff"><path d="M2 4 Q7 0 12 4"/><path d="M7 2 L3 13"/></svg><b>HEADING 1</b>Lorem ipsum dolor sit amet, te ullum corpora delicata duo. Rebum insolens pri eu.</div>
      <div class="tile" style="background:var(--green)"><svg viewBox="0 0 14 14" fill="none" stroke="#fff"><circle cx="7" cy="6" r="4"/><path d="M5 11h4M5.5 13h3"/></svg><b>HEADING 2</b>Lorem ipsum dolor sit amet, te ullum corpora delicata duo. Rebum insolens pri eu.</div>
      <div class="tile" style="background:var(--teal)"><svg viewBox="0 0 14 14" fill="none" stroke="#fff"><path d="M7 1 C7 1 3 7 3 9 A4 4 0 0 0 11 9 C11 7 7 1 7 1Z"/></svg><b>HEADING 3</b>Lorem ipsum dolor sit amet, te ullum corpora delicata duo. Rebum insolens pri eu.</div>
      <div class="tile" style="background:var(--slate)"><svg viewBox="0 0 14 14" fill="none" stroke="#fff"><rect x="3" y="2" width="8" height="11"/><path d="M5 5h4M5 7.5h4M5 10h4"/></svg><b>HEADING 4</b>Lorem ipsum dolor sit amet, te ullum corpora delicata duo. Rebum insolens pri eu.</div>
    </div>
    <div class="foot-brand">Terraquest NW</div><div class="page-no">12</div><div class="stripe"></div>
  </section>

  <section class="slide right-col">
    <h3 class="slide-title">RIGHT COLUMN</h3>
    <div class="pic" role="img" aria-label="Photo of a drone hovering over a snowy forest" style="top:40px;background:linear-gradient(180deg,#cfd8df,#8d9a8c)"></div>
    <div class="pic-note" style="top:40px;background:var(--orange)">Lorem ipsum dolor sit amet, te ullum corpora delicata duo. Rebum insolens pri eu.</div>
    <div class="pic" role="img" aria-label="Photo of a field researcher in winter woods" style="top:94px;background:linear-gradient(180deg,#dfe3e6,#6f6a66)"></div>
    <div class="pic-note" style="top:94px;background:var(--green)">Lorem ipsum dolor sit amet, te ullum corpora delicata duo. Rebum insolens pri eu.</div>
    <div class="col body" style="left:160px;right:18px;top:36px">
      <div class="kicker">Lorem ipsum</div>
      <ul>
        <li>Lorem ipsum dolor sit amet, te ullum corpora delicata duo. Rebum insolens pri eu. No alia tota modus qui.</li>
        <li class="sub">Sint brute at usu. Duo lisque appareat adversarium at.</li>
        <li>Lorem ipsum dolor sit amet, te ullum corpora delicata duo. Rebum insolens pri eu. No alia tota modus qui.</li>
        <li class="sub">Sint brute at usu. Duo lisque appareat adversarium at.</li>
      </ul>
    </div>
    <div class="foot-brand">Terraquest NW</div><div class="page-no">13</div><div class="stripe"></div>
  </section>

  <section class="slide">
    <h3 class="slide-title">TABLE SAMPLE</h3>
    <table class="sample">
      <tr><th>Lorem ipsum</th><th>Lorem ipsum 1</th><th>Lorem ipsum 2</th><th>Lorem ipsum 3</th></tr>
      <tr><td>Lorem ipsum dolor sit amet, consectetur adipiscing elit.</td><td>Lorem ipsum dolor sit amet, consectetur adipiscing elit.</td><td>Lorem ipsum dolor sit amet, consectetur adipiscing elit.</td><td>Lorem ipsum dolor sit amet, consectetur adipiscing elit.</td></tr>
      <tr><td>Lorem ipsum dolor sit amet, consectetur elit.</td><td>Lorem ipsum dolor sit amet, consectetur elit.</td><td>Lorem ipsum dolor sit amet, consectetur elit.</td><td>Lorem ipsum dolor sit amet, consectetur elit.</td></tr>
      <tr><td>Lorem ipsum dolor sit amet, consectetur adipiscing elit.</td><td>Lorem ipsum dolor sit amet, consectetur adipiscing elit.</td><td>Lorem ipsum dolor sit amet, consectetur adipiscing elit.</td><td>Lorem ipsum dolor sit amet, consectetur adipiscing elit.</td></tr>
      <tr><td>Lorem ipsum dolor sit amet, consectetur elit.</td><td>Lorem ipsum dolor sit amet, consectetur elit.</td><td>Lorem ipsum dolor sit amet, consectetur elit.</td><td>Lorem ipsum dolor sit amet, consectetur elit.</td></tr>
    </table>
    <div class="foot-brand">Terraquest NW</div><div class="page-no">14</div><div class="stripe"></div>
  </section>

  <section class="slide">
    <h3 class="slide-title">OUR SERVICES</h3>
    <div class="services">
      <div class="svc"><div class="dot" style="background:var(--orange)"><span></span></div><b>Heading 1</b><p>Lorem ipsum dolor sit amet,<br>consectetur adipiscing elit</p></div>
      <div class="svc"><div class="dot" style="background:var(--green)"><span></span></div><b>Heading 2</b><p>Lorem ipsum dolor sit amet,<br>consectetur adipiscing elit</p></div>
      <div class="svc"><div class="dot" style="background:var(--teal)"><span></span></div><b>Heading 3</b><p>Lorem ipsum dolor sit amet,<br>consectetur adipiscing elit</p></div>
      <div class="svc"><div class="dot" style="background:var(--slate)"><span></span></div><b>Heading 4</b><p>Lorem ipsum dolor sit amet,<br>consectetur adipiscing elit</p></div>
      <div class="svc"><div class="dot" style="background:var(--gold)"><span></span></div><b>Heading 5</b><p>Lorem ipsum dolor sit amet,<br>consectetur adipiscing elit</p></div>
      <div class="svc"><div class="dot" style="background:var(--navy)"><span></span></div><b>Heading 6</b><p>Lorem ipsum dolor sit amet,<br>consectetur adipiscing elit</p></div>
    </div>
    <div class="foot-brand">Terraquest NW</div><div class="page-no">15</div><div class="stripe"></div>
  </section>

  <section class="slide">
    <h3 class="slide-title">FINANCIAL DATA / PIE CHART</h3>
    <div class="chart-cap">Lorem ipsum dolar sit amet</div>
    <div class="pie"></div>
    <span class="pie-lbl" style="left:200px;top:94px">58%</span>
    <span class="pie-lbl" style="left:142px;top:108px">23%</span>
    <span class="pie-lbl" style="left:150px;top:72px">10%</span>
    <span class="pie-lbl" style="left:172px;top:56px;font-size:4px">9%</span>
    <div class="callout" style="left:40px;top:60px"><b>Heading 1</b><br>Lorem ipsum dolor sit amet</div>
    <div class="callout" style="left:70px;top:82px"><b>Heading 2</b><br>Lorem ipsum dolor sit amet</div>
    <div class="callout" style="left:60px;top:120px"><b>Heading 3</b><br>Lorem ipsum dolor sit amet</div>
    <div class="callout" style="left:244px;top:80px"><b>Heading 4</b><br>Lorem ipsum dolor sit amet</div>
    <div class="legend">● Lorem ipsum &nbsp; ● Lorem ipsum &nbsp; ● Lorem ipsum &nbsp; ● Lorem ipsum</div>
    <div class="foot-brand">Terraquest NW</div><div class="page-no">16</div><div class="stripe"></div>
  </section>

  <section class="slide">
    <h3 class="slide-title">BAR CHART SAMPLE</h3>
    <div class="chart-cap">Lorem ipsum dolor sit amet</div>
    <div class="bars">
      <i style="height:78%;background:var(--orange)"></i>
      <i style="height:44%;background:var(--green)"></i>
      <i style="height:62%;background:var(--teal)"></i>
      <i style="height:80%;background:var(--slate)"></i>
      <i style="height:44%;background:var(--gold)"></i>
      <i style="height:26%;background:var(--navy)"></i>
    </div>
    <div class="bar-axis"><span>Category 1</span><span>Category 2</span><span>Category 3</span><span>Category 4</span><span>Category 5</span><span>Category 6</span></div>
    <div class="foot-brand">Terraquest NW</div><div class="page-no">17</div><div class="stripe"></div>
  </section>

  <section class="slide">
    <h3 class="slide-title">TIMELINE SAMPLE</h3>
    <div class="timeline"></div>
    <span class="tl-lbl" style="left:18px;top:90px">2019</span>
    <span class="tl-lbl" style="right:18px;top:90px">2020</span>
    <span class="tl-dot" style="left:22px"></span><span class="tl-dot" style="left:122px"></span><span class="tl-dot" style="left:205px"></span><span class="tl-dot" style="left:262px"></span><span class="tl-dot" style="right:22px"></span>
    <span class="tl-lbl" style="left:70px;top:104px">JAN</span>
    <span class="tl-lbl" style="left:130px;top:90px">FEB</span>
    <span class="tl-lbl" style="left:190px;top:104px">MAR</span>
    <span class="tl-lbl" style="left:268px;top:90px">APR</span>
    <div class="tl-note" style="left:80px;top:58px;background:var(--orange)"><b>Heading 1</b>Lorem ipsum dolor sit amet, consectetur</div>
    <div class="tl-note" style="left:122px;top:108px;background:var(--green)"><b>Heading 2</b>Lorem ipsum dolor sit amet, consectetur</div>
    <div class="tl-note" style="left:210px;top:58px;background:var(--teal)"><b>Heading 3</b>Lorem ipsum dolor sit amet, consectetur</div>
    <div class="tl-note" style="left:262px;top:108px;background:var(--slate)"><b>Heading 4</b>Lorem ipsum dolor sit amet, consectetur</div>
    <div class="foot-brand">Terraquest NW</div><div class="page-no">18</div><div class="stripe"></div>
  </section>

  <section class="slide">
    <h3 class="slide-title">WORLD MAPS SAMPLE</h3>
    <div class="map-wash" role="img" aria-label="Light grey world map"></div>
    <div class="stat" style="left:72px;top:58px;width:38px;height:38px;background:var(--green);font-size:8px">68%</div>
    <div class="stat" style="left:98px;top:88px;width:30px;height:30px;background:var(--teal);font-size:7px">35%</div>
    <div class="stat" style="left:258px;top:72px;width:24px;height:24px;background:var(--orange);font-size:5px">15%</div>
    <div class="callout" style="left:18px;top:136px;width:80px"><b style="color:var(--orange)">MAPS REPORT</b><br>Lorem ipsum dolor sit amet, te ullum corpora delicata duo.</div>
    <div class="legend">● Legend 1 &nbsp; ● Legend 2 &nbsp; ● Legend 3</div>
    <div class="foot-brand">Terraquest NW</div><div class="page-no">19</div><div class="stripe"></div>
  </section>

  <section class="slide">
    <h3 class="slide-title">GRAPHIC SAMPLE</h3>
    <div class="hub"></div>
    <span class="hub-label">Terraquest NW</span>
    <span class="node" style="left:176px;top:56px;border-color:var(--orange)"></span>
    <span class="node" style="left:205px;top:72px;border-color:var(--green)"></span>
    <span class="node" style="left:205px;top:104px;border-color:var(--teal)"></span>
    <span class="node" style="left:176px;top:120px;border-color:var(--slate)"></span>
    <span class="node" style="left:146px;top:104px;border-color:var(--gold)"></span>
    <span class="node" style="left:146px;top:72px;border-color:var(--muted)"></span>
    <div class="node-text" style="left:147px;top:36px;text-align:center">Lorem ipsum dolor sit amet, consectetur adipiscing elit</div>
    <div class="node-text" style="left:225px;top:72px">Lorem ipsum dolor sit amet, consectetur adipiscing elit</div>
    <div class="node-text" style="left:225px;top:104px">Lorem ipsum dolor sit amet, consectetur adipiscing elit</div>
    <div class="node-text" style="left:147px;top:138px;text-align:center">Lorem ipsum dolor sit amet, consectetur adipiscing elit</div>
    <div class="node-text" style="left:70px;top:104px;text-align:right">Lorem ipsum dolor sit amet, consectetur adipiscing elit</div>
    <div class="node-text" style="left:70px;top:72px;text-align:right">Lorem ipsum dolor sit amet, consectetur adipiscing elit</div>
    <div class="foot-brand">Terraquest NW</div><div class="page-no">20</div><div class="stripe"></div>
  </section>

  <section class="slide thanks">
    <div class="photo-wash" role="img" aria-label="Muted photo of a helicopter over a forested slope" style="inset:0;background:radial-gradient(ellipse at 40% 25%,rgba(255,255,255,.08),transparent 55%)"></div>
    <div class="strip"></div>
    <h2>THANK YOU</h2>
    <div class="contact" style="left:75px"><svg viewBox="0 0 8 8"><path d="M4 0.5A2.6 2.6 0 0 0 1.4 3C1.4 5 4 7.5 4 7.5S6.6 5 6.6 3A2.6 2.6 0 0 0 4 0.5Z" fill="var(--orange)"/></svg><b>ADDRESS</b>1248 Ridgeway Ave<br>Kamloops, V2C 1A1</div>
    <div class="contact" style="left:147px"><svg viewBox="0 0 8 8" fill="none" stroke="var(--orange)" stroke-width=".7"><rect x=".8" y="1.8" width="6.4" height="4.4"/><path d="M.8 1.8L4 4.5L7.2 1.8"/></svg><b>EMAIL</b>hello@terraquestnw.org</div>
    <div class="contact" style="left:219px"><svg viewBox="0 0 8 8" fill="none" stroke="var(--orange)" stroke-width=".7"><rect x="2.4" y=".6" width="3.2" height="6.8" rx=".6"/></svg><b>PHONE</b>(250) 555 0142</div>
    <div class="closing">Lorem ipsum dolor sit amet, te ullum corpora delicata duo.<br>Rebum insolens pri eu. No alia tota modus qui.</div>
    <div class="stripe"></div>
  </section>

</main>
</body>
</html>
```